Home Health Company Needs a Corporate Identity Package

We need a corporate identity package (see what it should include below) for a home health care company. The design should be professional, uncluttered, simple and created in Publisher (so that we can edit the design in the future, if necessary. )
We need the following created:
-Presentation folder
-Business card template (color, double sided)
-Letterhead
-Stationary
-postcard sized marketing piece (5.5" x 8.5", color, double sided)

Target Market(s)

We are in the business of supplying personal care aids for in home care. Our services are directed towards older, retired individuals with some disability or illness. However, we will be marketing to the children or relatives of our in home clients. We want our logo to emphasize our reliability and personalized services.

Industry/Entity Type

Home Health Care

Requirements
Must have
• The design should be professional, uncluttered, simple and created in Publisher (so that we can edit the design in the future, if necessary. )

```html
<!DOCTYPE html>
<html lang="en">
<head>
<meta charset="utf-8">
<title>Brookfield Home Care – Identity Package</title>
<link rel="stylesheet" href="https://fonts.googleapis.com/css2?family=Open+Sans:wght@400;600&display=swap">
<style>
  :root {
    --backdrop: #e8e8ea;
    --paper: #fbfbfb;
    --charcoal: #2a2a2c;
    --charcoal-light: #48484b;
    --brand-blue: #3aa7cf;
    --ink: #3a3a3a;
    --ink-soft: #6a6a6a;
    --rule: #8a8a8a;
  }
  * { box-sizing: border-box; margin: 0; padding: 0; }
  html, body { width: 1200px; height: 859px; overflow: hidden; }
  body {
    background: var(--backdrop);
    font-family: "Open Sans", sans-serif;
    color: var(--ink);
    position: relative;
  }
  .piece { position: absolute; background: var(--paper); box-shadow: 0 2px 6px rgba(0,0,0,.12); }

  /* brand name lockup */
  .brand { display: flex; align-items: center; gap: 6px; color: var(--brand-blue); font-weight: 600; line-height: 1; }
  .brand-dot { border-radius: 50%; background: var(--brand-blue); flex: none; }
  .brand-sm { font-size: 11px; }
  .brand-sm .brand-dot { width: 9px; height: 9px; }
  .brand-md { font-size: 14px; }
  .brand-md .brand-dot { width: 12px; height: 12px; }
  .brand-lg { font-size: 34px; gap: 14px; }
  .brand-lg .brand-dot { width: 30px; height: 30px; }

  /* business cards */
  .card { width: 200px; height: 114px; left: 50px; }
  .card-front { top: 230px; background: var(--charcoal); display: flex; align-items: center; justify-content: center; }
  .card-back { top: 370px; padding: 14px 16px; }
  .card-back .brand { margin-bottom: 14px; }
  .card-details { font-size: 8px; line-height: 1.55; color: var(--ink-soft); }
  .card-details strong { color: var(--ink); font-weight: 600; }

  /* letterhead */
  .letterhead { left: 300px; top: 40px; width: 340px; height: 460px; padding: 24px 28px; font-size: 6.5px; line-height: 1.6; }
  .letterhead-top { display: flex; align-items: flex-end; gap: 10px; margin-bottom: 14px; }
  .letterhead-top .rule { flex: 1; height: 1px; background: var(--rule); margin-bottom: 3px; }
  .letter-sender { margin-bottom: 10px; color: var(--ink-soft); }
  .letter-body p { margin-bottom: 8px; }
  .letter-footer { position: absolute; left: 28px; right: 28px; bottom: 22px; border-top: 1px solid var(--rule); padding-top: 5px; font-size: 6.5px; color: var(--ink-soft); text-align: center; }

  /* envelope */
  .envelope { left: 300px; top: 540px; width: 370px; height: 190px; }
  .envelope .brand { position: absolute; right: 24px; top: 22px; }
  .envelope-address { position: absolute; left: 20px; right: 20px; bottom: 22px; border-bottom: 1px solid var(--rule); padding-bottom: 4px; font-size: 7px; color: var(--ink-soft); }

  /* presentation folder */
  .folder { left: 700px; top: 40px; width: 430px; height: 560px; background: linear-gradient(160deg, var(--charcoal-light), var(--charcoal) 70%); display: flex; align-items: center; justify-content: center; }

  /* mailer envelope with dark flap band */
  .mailer { left: 700px; top: 630px; width: 430px; height: 200px; }
  .mailer-band { height: 70px; background: var(--charcoal); display: flex; align-items: center; justify-content: center; }
  .mailer-rule { position: absolute; left: 20px; right: 20px; bottom: 24px; height: 1px; background: var(--rule); }
</style>
</head>
<body>

  <section class="piece card card-front" aria-label="Business card front">
    <div class="brand brand-md"><span class="brand-dot"></span>Brookfield Home Care</div>
  </section>

  <section class="piece card card-back" aria-label="Business card back">
    <div class="brand brand-sm"><span class="brand-dot"></span>Brookfield Home Care</div>
    <div class="card-details">
      <strong>Dana Brooks</strong><br>
      Care Coordinator<br>
      T 555.210.4400<br>
      E dana@brookfieldcare.com
    </div>
  </section>

  <section class="piece letterhead" aria-label="Letterhead">
    <div class="letterhead-top">
      <div class="brand brand-md"><span class="brand-dot"></span>Brookfield Home Care</div>
      <span class="rule"></span>
    </div>
    <div class="letter-sender">48 Harbor Lane<br>Riverton, OR 97401</div>
    <div class="letter-body">
      <p>March 12th, 2025</p>
      <p>Ms. Carter<br>Director, Elm Valley Family Center<br>12 Linden Road<br>Salem, OR 97301</p>
      <p>Dear Ms. Carter,</p>
      <p>The opening paragraph gives a short introduction and states the purpose of this letter in plain and friendly terms.</p>
      <p>The middle paragraph explains the details, supports the main point and keeps each sentence short and clear.</p>
      <p>The closing paragraph sums up the letter and thanks the reader.</p>
      <p>Sincerely,<br><br>Jordan Ellis</p>
    </div>
    <div class="letter-footer">210 River Street, Suite 400, Riverton, OR 97401 | 555.210.4400</div>
  </section>

  <section class="piece envelope" aria-label="Envelope">
    <div class="brand brand-md"><span class="brand-dot"></span>Brookfield Home Care</div>
    <div class="envelope-address">210 River Street, Suite 400, Riverton, OR 97401 | 555.210.4400</div>
  </section>

  <section class="piece folder" aria-label="Presentation folder">
    <div class="brand brand-lg"><span class="brand-dot"></span>Brookfield Home Care</div>
  </section>

  <section class="piece mailer" aria-label="Mailing envelope">
    <div class="mailer-band">
      <div class="brand brand-md"><span class="brand-dot"></span>Brookfield Home Care</div>
    </div>
    <span class="mailer-rule"></span>
  </section>

</body>
</html>
```